"ZENTRAL BEAT" - German Rap Concert

Hello,

I need a Flyer for a concert in Reutlingen, Germany.
The following Information should be included in the Flyer:

"ZENTRAL BEAT

09.01.2015
Beginn: 17:00 Uhr
Einlass: 15:30 Uhr

Acts:
OLU BRANDT
Mira Quell
Rotfeld & SolarBoy
RUV
Salihu. PNW & Luppo
TwoStep

VVK: 26€

Klangwerk, Lindenweg 14, 72760 Reutlingen"

The Logo of the Location should also be in the Flyer.
Main Act is Olu Brandt. you can find a Picture of him attached.
We also need space for Sponsoring-logos (4) at the bottom of the Flyer.
The Logos of the Sponsors will come later.

I hope you can understand my english ;)
If you have any questions, just write me an email.

Thanks in advance!

Tobias

Edit: The size of the Flyer should be DinA6.
I have also uploaded a better Version of the Klangwerk Logo!
Updates

Dear Designers, I have uploaded 3 of the 4 Sponsoring-Logos. Please insert them into the Flyer! Sponsors: LDR-S (please write under the logo "Sport- & Eventmanagement") Moos Brauerei Wendlinger Thanks!

```html
<!DOCTYPE html>
<html lang="de">
<head>
<meta charset="utf-8">
<title>Zentral Beat – Flyer</title>
<link rel="stylesheet" href="https://fonts.googleapis.com/css2?family=Archivo+Black&family=Roboto+Condensed:wght@400;700&family=Stardos+Stencil:wght@700&family=Archivo:wght@600&display=swap">
<style>
  :root {
    --page: #ffffff;
    --ink: #0b0b0c;
    --night: #121214;
    --red: #d0232a;
    --red-deep: #8e1518;
    --white: #ffffff;
    --teal: #5fc4b4;
    --grey: #96969a;
    --navy: #1f3a78;
    --frame: #8a8a8a;
  }
  * { margin: 0; padding: 0; box-sizing: border-box; }
  html, body { width: 1200px; height: 1000px; overflow: hidden; background: var(--page); }
  .flyer {
    position: absolute; left: 290px; top: 63px; width: 620px; height: 874px;
    border: 1px solid var(--frame); background: var(--night); overflow: hidden;
  }
  .artist-photo {
    position: absolute; left: 0; top: 0; width: 100%; height: 678px;
    background:
      radial-gradient(ellipse 180px 240px at 390px 320px, #3a3230 0%, rgba(30,28,30,0.6) 55%, transparent 80%),
      radial-gradient(ellipse 320px 170px at 120px 460px, var(--red-deep) 0%, rgba(120,20,22,0.7) 45%, transparent 75%),
      radial-gradient(ellipse 80px 60px at 585px 420px, #9b1c20 0%, transparent 80%),
      linear-gradient(180deg, #0d0d0f 0%, #141416 50%, #1b1b1e 100%);
  }
  .venue { position: absolute; left: 24px; top: 26px; color: var(--white); }
  .venue-logo {
    display: flex; align-items: center; gap: 7px;
    font-family: "Archivo Black", sans-serif; font-size: 20px; letter-spacing: -0.5px;
  }
  .venue-logo .mark { width: 11px; height: 11px; background: var(--teal); }
  .venue-address {
    margin-top: 8px; font-family: "Roboto Condensed", sans-serif;
    font-size: 21px; line-height: 27px;
  }
  .presale {
    position: absolute; left: 24px; top: 182px; color: var(--white);
    font-family: "Archivo Black", sans-serif; font-size: 25px; letter-spacing: 0.5px;
  }
  .event-date {
    position: absolute; left: 0; width: 100%; top: 498px; text-align: center;
    color: var(--white); font-family: "Archivo Black", sans-serif; font-size: 28px; letter-spacing: 1px;
  }
  .event-times {
    position: absolute; left: 0; width: 100%; top: 532px; text-align: center;
    color: var(--red); font-family: "Roboto Condensed", sans-serif; font-size: 19px;
  }
  .event-title {
    position: absolute; left: 0; width: 100%; top: 548px; text-align: center;
    color: var(--white); font-family: "Stardos Stencil", sans-serif; font-weight: 700;
    font-size: 78px; letter-spacing: 3px; line-height: 84px;
  }
  .headliner-bar { position: absolute; left: 0; top: 678px; width: 100%; height: 16px; background: var(--ink); }
  .headliner-tab { position: absolute; left: 162px; top: 641px; }
  .headliner {
    position: absolute; left: 162px; top: 648px; width: 300px; text-align: center;
    color: var(--ink); font-family: "Archivo Black", sans-serif; font-size: 31px; letter-spacing: 0.5px;
  }
  .lineup {
    position: absolute; left: 0; top: 694px; width: 100%; height: 77px; background: var(--red);
    border-bottom: 5px solid var(--ink);
    color: var(--white); font-family: "Archivo", sans-serif; font-weight: 600;
    font-size: 22px; line-height: 31px; text-align: center; padding-top: 6px;
  }
  .sponsors {
    position: absolute; left: 0; top: 776px; width: 100%; height: 98px; background: var(--page);
  }
  .sponsors-label {
    position: absolute; left: 0; width: 100%; top: 10px; text-align: center;
    font-family: "Archivo", sans-serif; font-weight: 600; font-size: 11px; color: var(--ink);
  }
  .sponsor { position: absolute; font-family: "Roboto Condensed", sans-serif; color: var(--ink); }
  .sponsor-brewery { left: 72px; top: 24px; display: flex; align-items: center; gap: 5px; font-size: 13px; font-weight: 700; }
  .sponsor-brewery .mark { width: 52px; height: 52px; border-radius: 50%; background: #cfcfcf; }
  .sponsor-juice {
    left: 163px; top: 32px; width: 134px; height: 33px; background: var(--navy);
    color: var(--white); font-size: 19px; font-weight: 700; display: flex; align-items: center; justify-content: center;
  }
  .sponsor-pending { left: 318px; top: 33px; width: 102px; height: 30px; background: var(--grey); }
  .sponsor-event { left: 438px; top: 28px; width: 130px; text-align: center; }
  .sponsor-event .name { font-size: 18px; font-weight: 700; }
  .sponsor-event .tagline { font-size: 10px; font-weight: 400; margin-top: 2px; }
</style>
</head>
<body>
  <main class="flyer">
    <div class="artist-photo" role="img" aria-label="Portrait of headliner Olu Brandt in dark mesh shirt and sunglasses against a dark background with red smoke"></div>

    <div class="venue">
      <div class="venue-logo"><span class="mark"></span>KLANGWERK</div>
      <div class="venue-address">Lindenweg 14<br>72760<br>Reutlingen</div>
    </div>

    <div class="presale">VVK: 26€</div>

    <div class="event-date">09.01.2015</div>
    <div class="event-times">Beginn: 17:00 Uhr – Einlass: 15:30 Uhr</div>
    <h1 class="event-title">ZENTRAL BEAT</h1>

    <div class="headliner-bar"></div>
    <svg class="headliner-tab" width="300" height="54" viewBox="0 0 300 54" aria-hidden="true">
      <polygon points="14,0 286,0 300,54 0,54" fill="#d0232a"/>
    </svg>
    <div class="headliner">OLU BRANDT</div>

    <div class="lineup">
      MIRA QUELL • ROTFELD &amp; SOLARBOY • RUV<br>
      SALIHU. PNW &amp; LUPPO • TWOSTEP
    </div>

    <section class="sponsors">
      <div class="sponsors-label">SPONSORS:</div>
      <div class="sponsor sponsor-brewery"><span class="mark"></span></div>
      <div class="sponsor sponsor-brewery" style="left:128px;top:42px;font-size:0"></div>
      <div class="sponsor sponsor-juice">Wendlinger</div>
      <div class="sponsor sponsor-pending"></div>
      <div class="sponsor sponsor-event">
        <div class="name">LDR-S</div>
        <div class="tagline">Sport- &amp; Eventmanagement</div>
      </div>
      <div class="sponsor" style="left:70px;top:80px;width:60px;text-align:center;font-size:9px;font-weight:700;">Moos Brauerei</div>
    </section>
  </main>
</body>
</html>
```